Need a Modern, Professional Website Design for Life Coaching Company in United States

Need Life Coaching Website Design for Life Coaching Company in the United States to wow and attract clients. Need a modern professional website to land clients.
- I am looking for an inspirational-looking website. Most of my clients will be female, but I want to attract both male and female clients, but I want to more females, site should be more feminine that masculine but attract both.

Target Market(s)

Adult women and men age 30 - 58

Colors
0054AA
0677BA
7BADD7
CADEEF
E8F1F8

Requirements
Must have
• modern, professional feel

```html
<!DOCTYPE html>
<html lang="en">
<head>
<meta charset="utf-8">
<title>Forward Path Coaching</title>
<link rel="stylesheet" href="https://fonts.googleapis.com/css2?family=Poppins:wght@500;600;700;800&family=IBM+Plex+Sans:wght@400;500&display=swap">
<style>
:root{
  --blue-dark:#0054AA;
  --blue:#0677BA;
  --blue-mid:#7BADD7;
  --blue-light:#CADEEF;
  --blue-pale:#E8F1F8;
  --ink:#1c1c1c;
  --text:#333;
  --white:#fff;
}
*{margin:0;padding:0;box-sizing:border-box}
html,body{width:1200px;height:4115px;overflow:hidden}
body{position:relative;font-family:"IBM Plex Sans",sans-serif;color:var(--text);background:var(--white)}
h1,h2,h3{font-family:"Poppins",sans-serif}
.rule{position:absolute;height:3px;width:34px;background:var(--blue)}

/* header + hero */
.hero{position:absolute;left:0;top:0;width:1200px;height:653px;
  background:linear-gradient(180deg,#d9a35a 0%,#e7b776 30%,#c9c4b4 55%,#8fa4b4 75%,#98a7b3 100%)}
.hero-photo{position:absolute;left:0;top:0;width:1200px;height:653px;
  background:radial-gradient(ellipse 260px 360px at 400px 400px,rgba(200,110,20,.55),rgba(200,110,20,0) 70%)}
.brand{position:absolute;font-family:"Poppins",sans-serif;font-weight:700;color:var(--blue-dark);line-height:1;text-align:center}
.brand .name{display:block;font-size:32px;letter-spacing:.5px}
.brand .sub{display:block;font-size:18px;letter-spacing:1px;margin-top:4px}
.nav{position:absolute;top:29px;left:572px;display:flex;font-size:15px}
.nav a{color:#222;text-decoration:none;padding:6px 16px}
.nav a.active{background:var(--blue-dark);color:#fff;padding:6px 12px}
.hero-title{position:absolute;left:650px;top:198px;width:440px;font-weight:800;font-size:37px;line-height:45px;color:var(--blue-dark)}
.hero-lead{position:absolute;left:650px;top:364px;width:440px;font-size:24px;line-height:37px;color:#1a1a1a}
.dots{position:absolute;left:562px;top:609px;display:flex;gap:7px}
.dots span{width:9px;height:9px;border-radius:50%;background:#fff}
.dots span.on{background:var(--blue-dark)}

/* services */
.section-title{position:absolute;left:0;width:1200px;text-align:center;font-weight:600;font-size:23px;color:var(--ink)}
.service{position:absolute;top:800px;width:120px;text-align:center;font-size:15px;line-height:19px;color:#333}
.service svg{display:block;margin:0 auto 18px}

/* about */
.about-photo{position:absolute;left:0;top:971px;width:1200px;height:502px;
  background:linear-gradient(90deg,#8a6248 0%,#c49a7c 25%,#e3d6c8 45%,#eef0f2 65%,#f4f6f8 100%)}
.about-title{position:absolute;left:787px;top:1073px;font-size:23px;font-weight:600;color:var(--ink)}
.about-copy{position:absolute;left:787px;top:1144px;width:276px;font-size:15px;line-height:22.5px;text-align:justify;color:#333}

/* how it works */
.how{position:absolute;left:0;top:1473px;width:1200px;height:934px;background:var(--blue-pale)}
.step{position:absolute;top:1624px;width:230px;height:230px}
.step-label{position:absolute;left:0;width:230px;text-align:center;font-family:"Poppins",sans-serif;font-weight:600;font-size:15px;line-height:18px;color:var(--blue)}
.how-copy{position:absolute;left:133px;top:1904px;width:467px;font-size:14px;line-height:22.4px;text-align:justify;color:#333}
.how-copy p+p{margin-top:22px}
.coach-photo{position:absolute;left:640px;top:1911px;width:426px;height:440px;
  background:linear-gradient(135deg,#4b4036 0%,#7f746a 35%,#b9c2cc 60%,#6a6f76 100%)}

/* benefits */
.benefits-band{position:absolute;left:0;top:2407px;width:1200px;height:388px;
  background:linear-gradient(180deg,#1d4f9f 0%,#0c46a4 45%,#0a3f96 75%,#164d97 100%)}
.benefits-title{position:absolute;left:0;top:2455px;width:1200px;text-align:center;color:#fff;font-size:23px;font-weight:600}
.benefit-list{position:absolute;top:2551px;width:387px;list-style:none}
.benefit-list li{position:relative;height:40px;padding:8px 0 0 28px;font-size:15px;color:#fff;border-bottom:1px solid rgba(255,255,255,.55)}
.benefit-list li:last-child{border-bottom:none}
.benefit-list svg{position:absolute;left:6px;top:11px}

/* welcome */
.welcome-photo{position:absolute;left:0;top:2795px;width:570px;height:503px;
  background:linear-gradient(160deg,#f2f2f2 0%,#e8e8e8 50%,#3a2d29 80%,#1d1818 100%)}
.welcome-title{position:absolute;left:678px;top:2852px;font-size:23px;font-weight:600;color:var(--ink)}
.welcome-copy{position:absolute;left:678px;top:2930px;width:387px;font-size:14px;line-height:22.4px;text-align:justify;color:#333}
.welcome-sign{position:absolute;left:678px;top:3196px;font-size:14px;line-height:22.4px;color:#333}

/* quote */
.quote{position:absolute;left:0;top:3298px;width:1200px;height:149px;background:var(--blue);text-align:center;color:#fff}
.quote h3{margin-top:28px;font-size:23px;font-weight:600}
.quote p{margin-top:4px;font-size:24px;color:#e8f1f8}

/* get started */
.start-band{position:absolute;left:0;top:3447px;width:1200px;height:483px;
  background:linear-gradient(180deg,#1e2a38 0%,#2e3d4f 35%,#3b4a58 60%,#2a3440 100%)}
.start-title{position:absolute;left:223px;top:3600px;width:300px;text-align:center;color:#fff;font-size:23px;font-weight:600}
.start-line{position:absolute;left:253px;top:3654px;width:220px;height:2px;background:#fff}
.start-copy{position:absolute;left:243px;top:3686px;width:262px;text-align:center;color:#fff;font-size:15.5px;line-height:21px}
.form{position:absolute;left:665px;top:3515px;width:356px;height:365px;background:#eef0f2}
.field{position:absolute;left:28px;width:300px;height:40px;background:#fff;border:1px solid #b9c3cc;font-size:12px;color:#333;padding:12px 14px}
.submit{position:absolute;left:28px;top:276px;width:300px;height:46px;background:var(--blue);color:#fff;font-family:"Poppins",sans-serif;font-weight:700;font-size:18px;text-align:center;line-height:46px}

/* footer */
.contact{position:absolute;top:3963px;display:flex;gap:12px;align-items:flex-start}
.contact small{display:block;font-family:"Poppins",sans-serif;font-weight:600;font-size:11px;color:var(--blue)}
.contact strong{display:block;font-family:"Poppins",sans-serif;font-weight:500;font-size:20px;color:var(--blue)}
.footer-rule{position:absolute;left:130px;top:4038px;width:938px;height:1px;background:#e3e6ea}
.copyright{position:absolute;left:0;top:4068px;width:1200px;text-align:center;font-size:11px;color:#444}
</style>
</head>
<body>

<!-- header + hero -->
<section class="hero">
  <div class="hero-photo" role="img" aria-label="Woman in an orange sweater with arms outstretched, facing the sun over the sea"></div>
  <div class="brand" style="left:130px;top:35px"><span class="name">FORWARD PATH</span><span class="sub">COACHING</span></div>
  <nav class="nav">
    <a class="active">Home</a><a>Coaching Services</a><a>FAQ</a><a>About Us</a><a>Contact Us</a>
  </nav>
  <h1 class="hero-title">Do you feel stuck or stagnant in reaching your goals?</h1>
  <p class="hero-lead">Gain clarity, confidence, accountability, and support to MOVE FORWARD and ACHIEVE SUCCESS!</p>
  <div class="dots"><span></span><span></span><span class="on"></span><span></span><span></span></div>
</section>

<!-- services -->
<h2 class="section-title" style="top:702px">Coaching Services to Help You Pivot and Prosper</h2>
<div class="rule" style="left:583px;top:758px"></div>

<div class="service" style="left:102px">
  <svg width="56" height="56" viewBox="0 0 56 56" fill="none" stroke="#0054AA" stroke-width="2.2" stroke-linecap="round"><circle cx="22" cy="12" r="5"/><path d="M22 18l-4 14 8 6M18 26l-8 4M22 22l10 2M8 48l40-32M40 16h8v8"/></svg>
  Career<br>Coaching</div>
<div class="service" style="left:227px">
  <svg width="56" height="56" viewBox="0 0 56 56" fill="none" stroke="#0054AA" stroke-width="2.2" stroke-linecap="round"><path d="M6 28L28 10l22 18M12 24v24h32V24"/><circle cx="22" cy="32" r="4"/><circle cx="34" cy="32" r="4"/><path d="M16 48c0-6 12-6 12 0M28 48c0-6 12-6 12 0M28 2v4M18 4l2 3M38 4l-2 3"/></svg>
  Relationship<br>Coaching</div>
<div class="service" style="left:355px">
  <svg width="56" height="56" viewBox="0 0 56 56" fill="none" stroke="#0054AA" stroke-width="2.2" stroke-linecap="round"><path d="M18 50V40c-6-4-8-10-6-18 2-8 10-12 18-11 9 1 14 8 13 16l4 7h-5v6h-8v4"/><circle cx="29" cy="24" r="7"/><path d="M29 4v3M16 8l2 3M42 8l-2 3"/></svg>
  Mindset<br>Coaching</div>
<div class="service" style="left:480px">
  <svg width="56" height="56" viewBox="0 0 56 56" fill="none" stroke="#0054AA" stroke-width="2.2" stroke-linecap="round"><circle cx="16" cy="10" r="5"/><path d="M10 20h12v16h-3v14h-6V36h-3zM30 14v28M36 18v20M42 22h10M48 18l4 4-4 4"/></svg>
  Resilience<br>Coaching</div>
<div class="service" style="left:608px">
  <svg width="56" height="56" viewBox="0 0 56 56" fill="none" stroke="#0054AA" stroke-width="2.2" stroke-linecap="round"><circle cx="28" cy="22" r="8"/><path d="M14 50c0-10 6-16 14-16s14 6 14 16M20 22l-8-6M36 22l8-6M28 4v6M10 8l4 4M46 8l-4 4"/></svg>
  Stress<br>Coaching</div>
<div class="service" style="left:733px">
  <svg width="56" height="56" viewBox="0 0 56 56" fill="none" stroke="#0054AA" stroke-width="2.2" stroke-linecap="round"><circle cx="28" cy="20" r="7"/><path d="M16 50V38l-6-10M40 50V38l6-10M16 38c4-6 20-6 24 0M28 4l2 4h4l-3 3 1 4-4-2-4 2 1-4-3-3h4z"/></svg>
  Confidence<br>Coaching</div>
<div class="service" style="left:860px">
  <svg width="56" height="56" viewBox="0 0 56 56" fill="none" stroke="#0054AA" stroke-width="2.2" stroke-linecap="round"><path d="M28 52S12 34 12 22a16 16 0 0132 0c0 12-16 30-16 30z"/><circle cx="28" cy="22" r="8"/><path d="M22 22h12M31 19l3 3-3 3"/></svg>
  Relocation<br>Coaching</div>
<div class="service" style="left:978px">
  <svg width="56" height="56" viewBox="0 0 56 56" fill="none" stroke="#0054AA" stroke-width="2.2" stroke-linecap="round"><path d="M20 52V42c-6-4-9-10-8-18 1-10 9-16 18-16 9 0 16 7 16 16l4 8h-5v6h-8v8"/><circle cx="30" cy="24" r="9"/><path d="M26 28c2-2 6-2 8 0"/></svg>
  Grief<br>Coaching</div>

<!-- about -->
<div class="about-photo" role="img" aria-label="Woman with curly hair, eyes closed, hands pressed together in reflection"></div>
<h2 class="about-title">About Us</h2>
<div class="rule" style="left:787px;top:1119px"></div>
<p class="about-copy">Forward Path Coaching offers coaching services for adult women and men willing and ready to work hard to create the life they crave. Whether you want to increase your confidence, discover your life’s purpose, land your dream job, or improve your relationships, we would be happy to help you reach your goals.</p>

<!-- how coaching works -->
<div class="how"></div>
<h2 class="section-title" style="top:1524px">How Coaching Works</h2>
<div class="rule" style="left:583px;top:1578px"></div>

<div class="step" style="left:125px">
  <svg width="230" height="230" viewBox="0 0 230 230" fill="none"><circle cx="115" cy="115" r="96" stroke="#0677BA" stroke-width="3" stroke-dasharray="330 273" transform="rotate(150 115 115)"/><circle cx="115" cy="115" r="110" stroke="#7BADD7" stroke-width="1.5" stroke-dasharray="260 431" transform="rotate(-30 115 115)"/>
  <path d="M104 60c-3 3-3 8 0 14 4 8 10 14 18 18 6 3 11 3 14 0l3-3-8-8-5 4c-5-2-10-7-12-12l4-5-8-8z" stroke="#0054AA" stroke-width="2.4"/><path d="M122 56a14 14 0 0112 12M122 64a6 6 0 015 5" stroke="#0054AA" stroke-width="2.4"/></svg>
  <div class="step-label" style="top:140px">Discovery Call</div>
</div>
<div class="step" style="left:361px">
  <svg width="230" height="230" viewBox="0 0 230 230" fill="none"><circle cx="115" cy="115" r="96" stroke="#0677BA" stroke-width="3" stroke-dasharray="330 273" transform="rotate(150 115 115)"/><circle cx="115" cy="115" r="110" stroke="#7BADD7" stroke-width="1.5" stroke-dasharray="260 431" transform="rotate(-30 115 115)"/>
  <rect x="94" y="56" width="44" height="30" rx="3" stroke="#0054AA" stroke-width="2.4"/><path d="M100 64h10M114 64h18M100 72h32M100 80h20" stroke="#0054AA" stroke-width="2"/><circle cx="103" cy="94" r="4" stroke="#0054AA" stroke-width="2"/></svg>
  <div class="step-label" style="top:136px">Sign Up</div>
</div>
<div class="step" style="left:605px">
  <svg width="230" height="230" viewBox="0 0 230 230" fill="none"><circle cx="115" cy="115" r="96" stroke="#0677BA" stroke-width="3" stroke-dasharray="330 273" transform="rotate(150 115 115)"/><circle cx="115" cy="115" r="110" stroke="#7BADD7" stroke-width="1.5" stroke-dasharray="260 431" transform="rotate(-30 115 115)"/>
  <path d="M100 54h24l8 8v36h-32z" stroke="#0054AA" stroke-width="2.4"/><path d="M105 68l2 2 4-4M105 78l2 2 4-4M105 88l2 2 4-4M115 68h11M115 78h11M115 88h11" stroke="#0054AA" stroke-width="2"/></svg>
  <div class="step-label" style="top:126px">Pre-Coaching<br>Questionnaire</div>
</div>
<div class="step" style="left:843px">
  <svg width="230" height="230" viewBox="0 0 230 230" fill="none"><circle cx="115" cy="115" r="96" stroke="#0677BA" stroke-width="3" stroke-dasharray="330 273" transform="rotate(150 115 115)"/><circle cx="115" cy="115" r="110" stroke="#7BADD7" stroke-width="1.5" stroke-dasharray="260 431" transform="rotate(-30 115 115)"/>
  <rect x="106" y="52" width="22" height="14" rx="2" stroke="#0054AA" stroke-width="2"/><circle cx="98" cy="74" r="5" stroke="#0054AA" stroke-width="2.2"/><circle cx="132" cy="74" r="5" stroke="#0054AA" stroke-width="2.2"/><path d="M88 98V86h20v12M122 98V86h20v12M104 84h22M112 84v14" stroke="#0054AA" stroke-width="2.2"/></svg>
  <div class="step-label" style="top:126px">1:1 Coaching<br>Session</div>
</div>

<div class="how-copy">
  <p>You can choose a 30 or 60-minute phone or video session. Forward Path Coaching offers a 90-Day Jump Start Coaching Program to help you set goals and take action. Individual coaching sessions range in price from $50.00 to $75.00. Deep down, you know you desire success. So, get started today! Get the life you crave!</p>
  <p>Like an athletic coach, a life coach comes alongside you to encourage, equip, and empower you to succeed. Your life coach will work with you to discover your passion, set realistic goals, create plans, and take action. Through goal-setting strategies, transformational coaching, and accountability, you will have a firm foundation to help you live a purposeful, abundant life.</p>
  <p>Life coaching is not a form of counseling. Counseling delves into your past behaviors and patterns. But life coaching is a future-oriented process – helping you close the gap between where you are now and where you desire to be. Life coaching focuses on your strengths and positive outlook. Life coaching is about goal setting for an already emotionally and mentally healthy person. Life coaching is not consulting; you do the self-development work for yourself.</p>
</div>
<div class="coach-photo" role="img" aria-label="Man with a headset taking notes beside a laptop during a video session"></div>

<!-- benefits -->
<div class="benefits-band" role="img" aria-label="Blue-toned mountain road through a forest"></div>
<h2 class="benefits-title">Benefits of Life Coaching Include</h2>
<div class="rule" style="left:583px;top:2507px;background:#fff"></div>
<ul class="benefit-list" style="left:150px">
  <li><svg width="16" height="14" viewBox="0 0 16 14"><path d="M1 7l5 5L15 1" fill="none" stroke="#fff" stroke-width="2.4"/></svg>Accountability and support to help you succeed</li>
  <li><svg width="16" height="14" viewBox="0 0 16 14"><path d="M1 7l5 5L15 1" fill="none" stroke="#fff" stroke-width="2.4"/></svg>Overcome obstacles</li>
  <li><svg width="16" height="14" viewBox="0 0 16 14"><path d="M1 7l5 5L15 1" fill="none" stroke="#fff" stroke-width="2.4"/></svg>Gain clarity about what you want</li>
  <li><svg width="16" height="14" viewBox="0 0 16 14"><path d="M1 7l5 5L15 1" fill="none" stroke="#fff" stroke-width="2.4"/></svg>Thrive from your God-given purpose</li>
  <li><svg width="16" height="14" viewBox="0 0 16 14"><path d="M1 7l5 5L15 1" fill="none" stroke="#fff" stroke-width="2.4"/></svg>Happiness from pursuing and reaching goals</li>
</ul>
<ul class="benefit-list" style="left:647px;width:421px">
  <li><svg width="16" height="14" viewBox="0 0 16 14"><path d="M1 7l5 5L15 1" fill="none" stroke="#fff" stroke-width="2.4"/></svg>Encouragement and guidance to help you stay on track</li>
  <li><svg width="16" height="14" viewBox="0 0 16 14"><path d="M1 7l5 5L15 1" fill="none" stroke="#fff" stroke-width="2.4"/></svg>Strategies to help you reach goals faster</li>
  <li><svg width="16" height="14" viewBox="0 0 16 14"><path d="M1 7l5 5L15 1" fill="none" stroke="#fff" stroke-width="2.4"/></svg>Energy from doing what excites</li>
  <li><svg width="16" height="14" viewBox="0 0 16 14"><path d="M1 7l5 5L15 1" fill="none" stroke="#fff" stroke-width="2.4"/></svg>Joy from doing what you love</li>
  <li><svg width="16" height="14" viewBox="0 0 16 14"><path d="M1 7l5 5L15 1" fill="none" stroke="#fff" stroke-width="2.4"/></svg>Increase productivity</li>
</ul>

<!-- welcome -->
<div class="welcome-photo" role="img" aria-label="Portrait of the coach, smiling, wearing glasses and a black top"></div>
<h2 class="welcome-title">Welcome</h2>
<div class="rule" style="left:678px;top:2897px"></div>
<p class="welcome-copy">Hi. I am Dana Ellison. I’m a life and career coach. I’m so excited that you are here, ready to take control of your destiny. Like you, I’ve experienced my share of life’s ups, downs, twists, and turns. To overcome those challenges, I remained committed, resilient, and optimistic about my goals and lifelong learning. Most importantly, I couldn’t give up because too much was at stake. I had to Move Forward. So, I am asking you, are you ready to Move Forward to live beyond your wildest dreams? If so, I invite you to contact me today to learn more. Let’s partner together and co-create your desired future.</p>
<p class="welcome-sign">Cheers!<br>Dana</p>

<!-- quote -->
<section class="quote">
  <h3>Inspirational Quote</h3>
  <p>When you are going through hell, keep going! ~ Anonymous</p>
</section>

<!-- get started -->
<div class="start-band" role="img" aria-label="Open road at dusk with trees and a cloudy sky"></div>
<h2 class="start-title">Get Started Today</h2>
<div class="start-line"></div>
<p class="start-copy">Request a free 15-minute phone consultation to see how we can help you achieve your goals. Step boldly into your greatness. Contact us today to start living a happier, more fulfilled, meaningful life.</p>
<form class="form">
  <div class="field" style="top:38px">Name</div>
  <div class="field" style="top:95px">Email Address</div>
  <div class="field" style="top:150px;height:110px">Comments</div>
  <div class="submit">Submit</div>
</form>

<!-- footer -->
<div class="brand" style="left:130px;top:3973px"><span class="name" style="font-size:27px">FORWARD PATH</span><span class="sub" style="font-size:15px">COACHING</span></div>
<div class="contact" style="left:660px">
  <svg width="22" height="22" viewBox="0 0 22 22" style="margin-top:14px"><circle cx="11" cy="11" r="11" fill="#0677BA"/><path d="M7 6c-1 1-1 3 0 5 1 2 3 4 5 5 2 1 3 1 4 0l1-1-2-2-2 1c-1-1-3-2-3-4l1-2-2-2z" fill="#fff"/></svg>
  <div><small>CALL US</small><strong>555-014-0199</strong></div>
</div>
<div class="contact" style="left:890px">
  <svg width="22" height="22" viewBox="0 0 22 22" style="margin-top:14px"><circle cx="11" cy="11" r="11" fill="#0677BA"/><path d="M11 17s-4-4-4-7a4 4 0 018 0c0 3-4 7-4 7z" fill="#fff"/><circle cx="11" cy="10" r="1.5" fill="#0677BA"/></svg>
  <div><small>Location</small><strong>Brookhaven, NC</strong></div>
</div>
<div class="footer-rule"></div>
<p class="copyright">Copyright © 2023 All Rights Reserved</p>

</body>
</html>
```